Introduction flyer

Bright Orchard Nutrition & Wellness Consulting, is a new holistic nutritional therapy specialising in womens health. I want a flyer that appeals to women between 15 to 60. It must speak "health, food & balance". I have attached the basic info I need included in the text. I like Greens & Blues, soft text. My flyer will be distributed to cafes, shops, fitness centres, hung up in grocery stores & health centres etc. The QEVR & WRUK logos need to appear on the flyer to show I am fully registered. My own logo & company name is attached.

Target Market(s)

Women from 10 to 60 years old.

Industry/Entity Type

Nutritionist

Colors
32a6d7
abd037
33b8a4
fbf289
ffcf3e
b768aa
d5d5d5
dcdcdc
e8e8e8

Requirements
Must have
• An image of healthy food & ladies. A group of women eating soup, stews or curry type dishes, with plenty of colour - no bread or white wine, and not just fruit please. Food that looks enjoyable to the average person.
• Nutrition is main part of my job, so please keep that in mind & emphasise food & natural well being.
Should not have
• People exercising, men, white wine, bread, cakes, sweets etc..

```html
<!DOCTYPE html>
<html lang="en">
<head>
<meta charset="utf-8">
<title>Bright Orchard Nutrition – Introduction Flyer</title>
<link href="https://fonts.googleapis.com/css2?family=Montserrat:ital,wght@0,400;0,500;0,700;1,400&display=swap" rel="stylesheet">
<style>
  :root {
    --teal: #1f9b8f;
    --teal-dark: #17867c;
    --lime: #a8cd2b;
    --ink: #1d1d1d;
    --backdrop: #e6e6e6;
    --paper: #ffffff;
    --brand-blue: #2a6fb4;
  }
  * { margin: 0; padding: 0; box-sizing: border-box; }
  html, body { width: 1200px; height: 798px; overflow: hidden; }
  body {
    background: var(--backdrop);
    font-family: "Montserrat", Arial, sans-serif;
    position: relative;
  }
  .flyer {
    position: absolute;
    left: 306px; top: 19px;
    width: 587px; height: 760px;
    background: var(--paper);
    overflow: hidden;
  }
  .photo {
    position: absolute; left: 0; top: 0; width: 587px; height: 560px;
    background:
      radial-gradient(ellipse at 60% 30%, #d8b89a 0%, rgba(216,184,154,0) 35%),
      linear-gradient(100deg, #a07a56 0%, #6c5a4a 30%, #3f4446 55%, #2f3537 75%, #8a8a86 100%);
  }
  .shapes { position: absolute; left: 0; top: 0; width: 587px; height: 760px; }
  .brand {
    position: absolute; left: 20px; top: 40px; width: 150px;
    text-align: center; color: var(--brand-blue);
  }
  .brand-mark {
    width: 26px; height: 26px; border-radius: 50%;
    background: var(--teal); margin: 0 auto 6px;
  }
  .brand-name { font-size: 8.5px; font-weight: 500; letter-spacing: .3px; line-height: 1.25; }
  .question {
    position: absolute; left: 0; top: 221px; width: 264px; height: 137px;
    background: rgba(31,155,143,.92); color: #fff;
    padding: 18px 0 0 21px;
  }
  .question h1 { font-size: 19.5px; font-weight: 700; line-height: 1.1; }
  .question p { font-size: 15.5px; font-weight: 400; line-height: 1.25; }
  .about {
    position: absolute; right: 27px; top: 434px; width: 255px;
    text-align: right; color: var(--teal);
  }
  .about h2 { font-size: 9px; font-weight: 700; line-height: 1.35; margin-bottom: 12px; }
  .about p { font-size: 7px; line-height: 1.38; margin-bottom: 22px; }
  .about h3 { font-size: 9px; font-weight: 700; line-height: 1.38; margin-bottom: 9px; }
  .specialisms { list-style: none; font-size: 7px; line-height: 1.36; }
  .specialisms li { padding-right: 8px; position: relative; }
  .specialisms li::after {
    content: ""; position: absolute; right: 0; top: 3px;
    width: 3.5px; height: 3.5px; border-radius: 50%; background: var(--teal);
  }
  .specialisms .note { font-size: 6px; font-style: italic; padding-right: 8px; }
  .specialisms .note::after { display: none; }
  .contact {
    position: absolute; left: 26px; top: 541px; width: 269px; height: 147px;
    border: 2.5px dotted var(--lime); border-radius: 10px;
    text-align: center; color: var(--ink); padding-top: 10px;
  }
  .contact .lead { font-size: 12px; font-weight: 700; }
  .contact .line { font-size: 12px; line-height: 1.25; }
  .contact .book { font-size: 7.5px; font-style: italic; line-height: 1.3; margin-top: 2px; }
  .contact .terms {
    font-size: 6.6px; font-style: italic; color: var(--lime);
    line-height: 1.4; margin-top: 9px; padding: 0 4px;
  }
  .memberships {
    position: absolute; left: 63px; top: 700px;
    display: flex; align-items: center; gap: 24px;
  }
  .member { display: flex; align-items: center; gap: 5px; font-size: 22px; font-weight: 700; }
  .member-mark { width: 26px; height: 26px; border-radius: 50%; }
  .member.wruk { color: var(--teal); }
  .member.wruk .member-mark { background: var(--teal); }
  .member.qevr { color: #5a2c86; }
  .member.qevr .member-mark { background: #5a2c86; }
</style>
</head>
<body>
  <main class="flyer">
    <div class="photo" role="img" aria-label="Photograph of a woman enjoying a bowl of soup at a café table"></div>

    <svg class="shapes" viewBox="0 0 587 760" aria-hidden="true">
      <path d="M0 0 H400 C300 60 160 120 0 135 Z" fill="#ffffff"/>
      <path d="M0 135 C160 120 300 60 400 0 H470 C340 90 170 155 0 166 Z" fill="var(--teal)"/>
      <path d="M0 166 C170 155 340 90 470 0 H490 C350 105 180 170 0 179 Z" fill="var(--lime)"/>
      <path d="M0 500 C160 425 380 385 587 366 V392 C400 402 200 455 0 550 Z" fill="var(--lime)"/>
      <path d="M0 550 C200 455 400 402 587 392 V760 H0 Z" fill="#ffffff"/>
    </svg>

    <div class="brand">
      <div class="brand-mark"></div>
      <div class="brand-name">BRIGHT ORCHARD NUTRITION<br>&amp; Wellness Consulting</div>
    </div>

    <section class="question">
      <h1>DO YOU EXPERIENCE</h1>
      <p>LOW ENERGY, LOW LIBIDO,<br>MENSTRUAL CYCLE<br>COMPLICATIONS, OR<br>ARE YOU PLANNING A BABY?</p>
    </section>

    <section class="about">
      <h2>SMALL CHANGES TO YOUR DIET MAY LEAD<br>TO BIG CHANGES IN YOUR HEALTH.</h2>
      <p>EAT WELL, LIVE WELL.<br>DISCOVER EXACTLY WHAT YOU NEED TO CHANGE<br>AND HOW TO MAKE THESE CHANGES LONG LASTING.<br>THERE IS NO 1 RULE-FITS-ALL. MY NUTRITIONAL<br>ADVICE AIMS TO DIG UP THE ROOT CAUSE TO MY CLI-<br>ENT'S HEALTH CONCERNS. MY LIFESTYLE PLANS ARE<br>COMPLETELY PERSONALISED TO AN INDIVIDUAL'S<br>NEEDS AND CIRCUMSTANCES. I CONSIDER THE<br>WHOLE PERSON NOT JUST SYMPTOMS OR DISEASE.</p>
      <h3>QUALIFIED, REGISTERED AND FULLY<br>INSURED NUTRITIONAL THERAPIST &amp;<br>WELLNESS CONSULTANT, SPECIALISING IN:</h3>
      <ul class="specialisms">
        <li>FERTILITY, IVF, PRE-CONCEPTION, PREGNANCY &amp; POST-NATAL<br>CARE</li>
        <li>MENSTRUAL CYCLE CHALLENGES</li>
        <li class="note">(PCOS, ENDOMETRIOSIS, PMS, HEAVY/IRREGULAR PERIODS ETC)</li>
        <li>THYROID CONDITIONS</li>
        <li>LOW LIBIDO</li>
        <li>DIGESTIVE HEALTH</li>
        <li>CHRONIC FATIGUE SYNDROME</li>
        <li>PERIMENOPAUSE/MENOPAUSE</li>
        <li>WEIGHT MANAGEMENT</li>
        <li>TYPE 2 DIABETES, BLOOD SUGAR DYSREGULATION, HIGH<br>BLOOD PRESSURE, HIGH CHOLESTEROL</li>
      </ul>
    </section>

    <section class="contact">
      <div class="lead">CALL MAEVE TODAY ON</div>
      <div class="line">085-2640-318</div>
      <div class="lead">OR EMAIL</div>
      <div class="line">MAEVE@BRIGHTORCHARDNUTRITION.IE</div>
      <div class="book">TO BOOK A CONSULTATION OR FOR A FREE NO<br>OBLIGATION 15-MINUTE MINI CONSULTATION.</div>
      <div class="terms">INITIAL CONSULTATIONS TYPICALLY LAST UP TO 2 HOURS, FOLLOW UPS 30 – 60 MINUTES. FURTHER INVESTIGATIVE TESTS MAY BE RECOMMENDED SUCH AS BLOOD, URINE, SALIVA SAMPLING. THESE WILL ALWAYS BE AGREED WITH THE CLIENT IN ADVANCE.</div>
    </section>

    <div class="memberships">
      <div class="member wruk"><span class="member-mark"></span>WRUK</div>
      <div class="member qevr"><span class="member-mark"></span>QEVR</div>
    </div>
  </main>
</body>
</html>
```